LABEL DESIGN NEEDED FOR Mabel Fenwick Cookies

I am starting a Cookie Company with my daughter Mabel that will begin by making chocolate chip cookies.
These labels will go on a 2.5 by 2x6 clear cellophane bag that we will use to give out samples of our cookies to others to introduce our new- company to them.
I want the label to be 2X3 for both the front and the back.
These labels are for a cookie business starting out by making chocolate chip cookies. We will start out using clear cellophane bags with gold twist ties.
The size of the bags we will be using at first are 2.5x2x6 and 3.5x2x7.5.
Again, the clear cellophane bags will contain chocolate chip cookies that are round and weigh 1.5 oz. each.
On the front of the label I want it to have my logo which says Mabel Fenwick Cookies (see attached) with the name of the cookie (Chocolate Chip) and the weight (3oz.)
On the back of the label I would like the following:
Ingredients: All-purpose Flour, Semisweet Chocolate Chips, Granulated Sugar, Light Brown Sugar, Butter, Egg yolk, Light Corn Syrup, Milk, Vanilla Extract, Baking Soda, Salt
We also need it to say:
These products were manufactured in a facility that processes nuts and other known allergens. i.e. Milk, Eggs, Wheat, Soy
and it needs to have my address:
Larkmont, West Arden 11893
I have attached three things which will help the artist:
1.Our company logo (Mabel Fenwick Cookies)
2.A front and back label of a packaging from a cookie company that I really liked and thought was very cute. This should give the artist a start in terms of what direction to head in.
Thank you so much for all your help and just let me know what I need to do next.

```html
<!DOCTYPE html>
<html lang="en">
<head>
<meta charset="utf-8">
<title>Mabel Fenwick Cookies – Back Label</title>
<link rel="stylesheet" href="https://fonts.googleapis.com/css2?family=Jost:wght@400;500&display=swap">
<style>
  :root {
    --orange: #e0823f;
    --chocolate: #3c2318;
    --text-light: #ffffff;
    --heading-orange: #e48a45;
  }
  html, body {
    margin: 0;
    padding: 0;
    overflow: hidden;
  }
  .label {
    position: relative;
    width: 1200px;
    height: 801px;
    background: var(--orange);
    overflow: hidden;
    font-family: "Jost", "Futura", sans-serif;
  }
  .drip-top {
    position: absolute;
    left: 0; top: 0;
    width: 1200px;
    height: 170px;
    background: linear-gradient(to bottom, var(--chocolate) 0%, var(--chocolate) 45%, rgba(60,35,24,0.55) 75%, rgba(60,35,24,0) 100%);
  }
  .drip-bottom {
    position: absolute;
    left: 0; bottom: 0;
    width: 1200px;
    height: 150px;
    background: linear-gradient(to top, var(--chocolate) 0%, var(--chocolate) 50%, rgba(60,35,24,0.55) 78%, rgba(60,35,24,0) 100%);
  }
  .ingredients-title {
    position: absolute;
    left: 75px; top: 242px;
    width: 583px; height: 52px;
    background: var(--chocolate);
    color: var(--heading-orange);
    font-size: 32px;
    font-weight: 400;
    letter-spacing: 2.5px;
    text-align: center;
    line-height: 54px;
    margin: 0;
  }
  .ingredients-list {
    position: absolute;
    left: 75px; top: 306px;
    width: 583px; height: 288px;
    box-sizing: border-box;
    padding: 10px 38px 0 26px;
    background: var(--chocolate);
    color: var(--text-light);
    font-size: 29px;
    line-height: 43.4px;
    letter-spacing: 1.5px;
    margin: 0;
  }
  .ingredients-list .line {
    display: block;
    text-align: justify;
    text-align-last: justify;
  }
  .ingredients-list .line.last {
    text-align-last: left;
  }
  .characters {
    position: absolute;
    left: 724px; top: 244px;
    width: 388px; height: 156px;
    background: radial-gradient(ellipse at center, rgba(255,240,210,0.35), rgba(224,130,63,0) 70%);
  }
  .allergen-note {
    position: absolute;
    left: 664px; top: 412px;
    width: 500px;
    margin: 0;
    color: var(--chocolate);
    font-size: 22px;
    line-height: 33.4px;
    letter-spacing: 1.9px;
    text-align: center;
  }
  .divider {
    position: absolute;
    left: 685px; top: 552px;
    width: 459px; height: 4px;
  }
  .address {
    position: absolute;
    left: 664px; top: 568px;
    width: 500px;
    margin: 0;
    color: var(--chocolate);
    font-size: 23px;
    letter-spacing: 2.4px;
    text-align: center;
  }
</style>
</head>
<body>
  <main class="label">
    <div class="drip-top" role="img" aria-label="Dripping chocolate border with cream swirls"></div>

    <h2 class="ingredients-title">INGRIDIENTS</h2>
    <p class="ingredients-list">
      <span class="line">All-purpose Flour, Semisweet</span>
      <span class="line">Chocolate Chips, Granulated</span>
      <span class="line">Sugar, Light Brown Sugar, Butter,</span>
      <span class="line">Egg yolk, Light Corn Syrup, Milk,</span>
      <span class="line">Vanilla Extract, Baking Soda,</span>
      <span class="line last">Salt.</span>
    </p>

    <div class="characters" role="img" aria-label="Cheerful cartoon baking ingredients: vanilla bottle, butter, sugar cube, flour sack, milk carton, cookie, chocolate chip and egg yolk"></div>

    <p class="allergen-note">These products were manufactured<br>in a facility that processes nuts and<br>other known allergens. i.e. Milk,<br>Eggs, Wheat, Soy</p>
    <svg class="divider" viewBox="0 0 459 4" aria-hidden="true">
      <line x1="0" y1="2" x2="459" y2="2" stroke="#3c2318" stroke-width="4" stroke-dasharray="11 6"/>
    </svg>
    <p class="address">Larkmont, West Arden 11893</p>

    <div class="drip-bottom" role="img" aria-label="Chocolate drops border with cream highlights"></div>
  </main>
</body>
</html>
```